Anzeigengestaltung für Immobilienmakler
Zielgruppe
Wir sind ein Immobilienmakler. Wir wollen eine Plakatkampagne starten. Dazu brauchen wir ein Plakat.
Ich habe noch ein Foto des Plakats hochgeladen, um die Situation zu verdeutlichen.
Aufgabenstellung
Die Maße sind als Anhang dabei. Außerdem dabei ist ein Beispiel eines unserer Werbeschilder (daraus bitte die Farbgebung übernehmen), sowie unser Logo.
Das Plakat sollte mit einem Spruch sein, gerne mit Witz, pfiffig - einfach ein Hingucker.

```html
<!DOCTYPE html>
<html lang="de">
<head>
<meta charset="utf-8">
<title>Plakat – Hartwig Immobilien</title>
<link href="https://fonts.googleapis.com/css2?family=Barlow:wght@300;400;600;700&display=swap" rel="stylesheet">
<style>
  :root {
    --dark: #29292d;
    --cream: #f2efe8;
    --beige: #b9ae98;
    --grey: #86857d;
    --page: #d9d9d9;
  }
  html, body {
    margin: 0;
    width: 831px;
    height: 1200px;
    overflow: hidden;
    background: var(--page);
  }
  .poster {
    position: absolute;
    left: 20px;
    top: 325px;
    width: 1392px;
    height: 967px;
    transform: scale(0.5682);
    transform-origin: 0 0;
    background: var(--cream);
    overflow: hidden;
    font-family: "Barlow", "Helvetica Neue", Arial, sans-serif;
  }
  .shapes { position: absolute; inset: 0; }
  .headline {
    position: absolute;
    left: 66px;
    top: 52px;
    margin: 0;
    color: var(--cream);
    font-weight: 700;
    font-size: 96px;
    line-height: 92px;
    letter-spacing: 6px;
  }
  .subline {
    position: absolute;
    left: 66px;
    top: 440px;
    margin: 0;
    color: var(--cream);
    font-weight: 400;
    font-size: 52px;
    line-height: 58px;
    letter-spacing: 1px;
  }
  .stat {
    position: absolute;
    top: 612px;
    width: 200px;
    text-align: center;
    color: var(--dark);
  }
  .stat svg { display: block; margin: 0 auto; height: 78px; }
  .stat-number { display: block; margin-top: 20px; font-size: 38px; font-weight: 700; line-height: 40px; }
  .stat-label { display: block; font-size: 18px; font-weight: 600; line-height: 24px; letter-spacing: 0.5px; }
  .divider { position: absolute; top: 620px; width: 4px; height: 180px; background: var(--dark); }
  .phone {
    position: absolute;
    left: 64px;
    top: 850px;
    display: flex;
    align-items: center;
    gap: 18px;
    color: var(--dark);
    font-size: 66px;
    font-weight: 700;
    letter-spacing: 1px;
  }
  .web {
    position: absolute;
    left: 752px;
    top: 862px;
    display: flex;
    align-items: center;
    gap: 16px;
    color: var(--cream);
    font-size: 46px;
    font-weight: 600;
  }
  .brand {
    position: absolute;
    left: 790px;
    top: 140px;
    width: 520px;
    text-align: center;
    color: var(--dark);
    font-weight: 600;
    font-size: 58px;
    line-height: 66px;
    letter-spacing: 4px;
  }
</style>
</head>
<body>
<div class="poster">
  <svg class="shapes" viewBox="0 0 1392 967" width="1392" height="967">
    <defs>
      <linearGradient id="photoTone" x1="0" y1="0" x2="1" y2="1">
        <stop offset="0" stop-color="#c9ccd0"/>
        <stop offset="0.45" stop-color="#6f7a82"/>
        <stop offset="0.75" stop-color="#e6cfc8"/>
        <stop offset="1" stop-color="#b9bcc0"/>
      </linearGradient>
      <linearGradient id="chevronShade" x1="0" y1="0" x2="1" y2="0">
        <stop offset="0" stop-color="#29292d"/>
        <stop offset="1" stop-color="#3a3a3f"/>
      </linearGradient>
    </defs>
    <polygon points="0,0 543,0 730,325 615,595 0,595" fill="url(#chevronShade)"/>
    <polygon points="0,0 520,0 700,325 590,595 0,595" fill="var(--dark)"/>
    <polygon role="img" aria-label="Foto: junges Paar hält ein kleines Holzhaus-Modell" points="768,345 1392,345 1392,850 636,850" fill="url(#photoTone)"/>
    <polygon points="0,595 878,595 796,825 0,825" fill="var(--beige)"/>
    <polygon points="646,850 1392,850 1392,967 694,967" fill="var(--dark)"/>
  </svg>

  <div class="brand">LENA HARTWIG<br>IMMOBILIEN</div>

  <h1 class="headline">WENN ES<br>UM IHRE<br>IMMOBILIE<br>GEHT,</h1>
  <p class="subline">SIND WIR DIE<br>RICHTIGEN FÜR SIE</p>

  <div class="stat" style="left:36px">
    <svg viewBox="0 0 80 80"><circle cx="40" cy="40" r="32" fill="none" stroke="var(--dark)" stroke-width="6"/><path d="M40 20 V42 L52 54" fill="none" stroke="var(--dark)" stroke-width="6" stroke-linecap="round"/></svg>
    <span class="stat-number">1997</span>
    <span class="stat-label">LANGJÄHRIGE<br>ERFAHRUNG SEIT</span>
  </div>
  <div class="divider" style="left:226px"></div>
  <div class="stat" style="left:238px">
    <svg viewBox="0 0 80 80"><path d="M6 18 H32 L38 26 H74 V66 H6 Z" fill="none" stroke="var(--dark)" stroke-width="5" stroke-linejoin="round"/></svg>
    <span class="stat-number">4021</span>
    <span class="stat-label">KAUFINTERESSENTEN<br>FÜR IHRE IMMOBILIE</span>
  </div>
  <div class="divider" style="left:448px"></div>
  <div class="stat" style="left:452px">
    <svg viewBox="0 0 80 80"><rect x="18" y="24" width="44" height="36" fill="none" stroke="var(--dark)" stroke-width="5"/><path d="M18 36 H62 M40 24 V36" stroke="var(--dark)" stroke-width="5"/></svg>
    <span class="stat-number">500+</span>
    <span class="stat-label">ABGESCHLOSSENE<br>FINANZIERUNGEN</span>
  </div>
  <div class="divider" style="left:648px"></div>
  <div class="stat" style="left:626px">
    <svg viewBox="0 0 80 80"><path d="M40 62 L16 38 A12 12 0 0 1 40 24 A12 12 0 0 1 64 38 Z" fill="none" stroke="var(--dark)" stroke-width="5" stroke-linejoin="round"/></svg>
    <span class="stat-number">1510</span>
    <span class="stat-label">GLÜCKLICHE<br>KUNDEN</span>
  </div>

  <div class="phone">
    <svg width="30" height="54" viewBox="0 0 30 54"><rect x="2.5" y="2.5" width="25" height="49" rx="4" fill="none" stroke="var(--dark)" stroke-width="5"/><rect x="2.5" y="42" width="25" height="9.5" fill="var(--dark)"/></svg>
    <span>07022 5550199</span>
  </div>

  <div class="web">
    <svg width="40" height="36" viewBox="0 0 40 36"><path d="M38 2 L2 18 L14 22 L18 34 L24 24 Z" fill="var(--cream)"/></svg>
    <span>LHartwig-immobilien.de</span>
  </div>
</div>
</body>
</html>
```